SHOP PAGE PRODUCT GRAPHICS 900x600 FOR E COMMERCE SITE. 5 TOTAL

NEED 5 GRAPHICS 900x600 MADE FOR MY SHOP PAGE HERE:

feel free to omit any redundant content http://pixelcratehub.com/qx/dorian/shop.jpg Custom Image For Products On Shop Page:AL A CARTE:Buy Video Ads On an As Needed Basis$37 PER VIDEO!INCLUDES:1 Video Ad ($149 VALUE) 1 Video Ad Converted To Square Ratio ($39 VALUE)1 Video Ad Converted To Vertical Ratio ($39 VALUE)1 Video Ad Converted To Chatterly Cover Video ($129 VALUE)VALUE $3564 Videos NOW ONLY $14960% OFF$37 PER VIDEO!INSTRUCTIONS FOR IMAGE:SHOW PHOTOS OF ALL PHOTOS SIZES USING SAME VIDEO. LET ME KNOW IF YOU NEED ONE I HAVE MP4 FILES FOR ALL SIZES SHOW PHOTOS OF ALL PHOTOS SIZES USING SAME VIDEO. LET ME KNOW IF YOU NEED ONE I HAVE MP4 FILES FOR ALL SIZES OR YOU CAN USE IMAGES FROM MY WEBSITE WWW.LARKREELSTUDIO.COM PLEASE SCROLL DOWN ON HOMEPAGE AND SEE “VIDEO SIZES” SECTION AND USE THESE IMAGES IF YOU HAVE TO….I WANT THE IMAGE TO SHOW ALL THE DIFFERENT VIDEO SIZES THEY GET SO IT LOOKS LIKE A LOT OF VALUE…._______________________________________________________________________________________SUBSCRIPTION:Big Discounts Per Video When You Sign Up For A Monthly Subscription$25 PER VIDEO!INCLUDES:1 Video Ad ($149 VALUE)1 Video Ad Converted To Square Ratio ($39 VALUE)1 Video Ad Converted To Vertical Ratio ($39 VALUE)1 Video Ad Converted To Chatterly Cover Video ($129 VALUE)VALUE $3564 Videos NOW ONLY $9975% OFF$25 PER VIDEO!INSTRUCTIONS FOR IMAGE:SHOW PHOTOS OF ALL PHOTOS SIZES USING SAME VIDEO. LET ME KNOW IF YOU NEED ONE I HAVE MP4 FILES FOR ALL SIZES SHOW PHOTOS OF ALL PHOTOS SIZES USING SAME VIDEO. LET ME KNOW IF YOU NEED ONE I HAVE MP4 FILES FOR ALL SIZES OR YOU CAN USE IMAGES FROM MY WEBSITE WWW.LARKREELSTUDIO.COM PLEASE SCROLL DOWN ON HOMEPAGE AND SEE “VIDEO SIEZES” SECTION AND USE THESE IMAGES IF YOU HAVE TO….I WANT THE IMAGE TO SHOW ALL THE DIFFERENT VIDEO SIZES THEY GET SO IT LOOKS LIKE A LOT OF VALUE….___________________________________________________________________________LARK MONTHLY CONTENT CALENDAR SUBSCRIPTION:Daily Content and Custom Branded Videos For Every Day.LESS THAN $10 PER VIDEO!INCLUDES:30 Videos ($1470 VALUE)VALUE $1470/mth30 Videos & Daily Content Only $299/mth90% OFF$10 PER VIDEO!INSTRUCTIONS FOR IMAGE:SHOW A PIC OF A CALENDAR WITH CONTENT/TEXT AND VIDEO FOR EACH DAY. SEE MY WEBSITE AT https://larkreelstudio.com/calendar/june and use something from here for this image. I WANT IT TO BE CLEAR THAT THEY WILL RECEIVE A VIDEO FOR EVERY DAY AND CONTENT TO POST TO THEIR SOCIAL MEDIA PAGES ______________________________________________________________________________HOLIDAY THEMED PACKAGECelebrate the Holidays with videos$58 PER VIDEO!INCLUDES:17 HOLIDAY THEMED VIDEOS ($1683 VALUE)VALUE $168317 Videos Only $99935% OFF$58 PER VIDEO!INSTRUCTIONS FOR IMAGE:SHOW A COLLAGE OF HOLIDAY THEMED VIDEOS. YOU CAN FIND SOME HOLIDAY THEMED VIDEOS ON MY WEBSITE HERE: https://larkreelstudio.com/categories FROM DROP DOWN MENU CHOOSE LABOR DAY, MEMORIAL DAY, HALLOWEEN, CHRISTMAS, NEW YEARS, NEW YEARS, VALENTINES TO SEE EXAMPLES OF HOLIDAY THEMED VIDEOS FOR THIS IMAGE. __________________________________________________________________SEASONAL THEMED PACKAGEWelcome every season with a new video$74 PER VIDEO!4 Seasonal Themed Videos ($396 VALUE)VALUE $3964 Videos Only $29925% OFF$74 PER VIDEO!INSTRUCTIONS FOR IMAGE:SHOW A COLLAGE OF SEASONAL THEMED VIDEOS. YOU CAN FIND THE SEASONAL THEMED VIDEOS ON MY WEBSITE CLIPNEST PAGE HERE: https://clipnest.com/user41527093 SUMMER, SPRING, FALL, WINTER

Target Market(s)

B2B

Industry/Entity Type

Video Production

Colors

Designer to choose colors to be used in the design.

Requirements
Must have
• NEED 5 GRAPHICS MADE FOR MY SHOP PAGE HERE: 900x600 ://pixelcratehub.com/qx/dorian/shop.jpg
• Custom Image For Products On Shop Page:
• AL A CARTE:
• Buy Video Ads On an As Needed Basis
• $37 PER VIDEO!
• INCLUDES:
• 1 Video Ad ($149 VALUE)
• 1 Video Ad Converted To Square Ratio ($39 VALUE)
• 1 Video Ad Converted To Vertical Ratio ($39 VALUE)
• 1 Video Ad Converted To Chatterly Cover Video ($129 VALUE)
• VALUE $356
• 4 Videos NOW ONLY $149
• 60% OFF
• $37 PER VIDEO!
• INSTRUCTIONS FOR IMAGE:
• SHOW PHOTOS OF ALL PHOTOS SIZES USING SAME VIDEO. LET ME KNOW IF YOU NEED ONE I HAVE MP4 FILES FOR ALL SIZES SHOW PHOTOS OF ALL PHOTOS SIZES USING SAME VIDEO. LET ME KNOW IF YOU NEED ONE I HAVE MP4 FILES FOR ALL SIZES OR YOU CAN USE IMAGES FROM MY WEBSITE WWW.LARKREELSTUDIO.COM PLEASE SCROLL DOWN ON HOMEPAGE AND SEE “VIDEO SIZES” SECTION AND USE THESE IMAGES IF YOU HAVE TO….I WANT THE IMAGE TO SHOW ALL THE DIFFERENT VIDEO SIZES THEY GET SO IT LOOKS LIKE A LOT OF VALUE….
• _______________________________________________________________________________________
• SUBSCRIPTION:
• Big Discounts Per Video When You Sign Up For A Monthly Subscription
• $25 PER VIDEO!
• INCLUDES:
• 1 Video Ad ($149 VALUE)
• VALUE $356
• 4 Videos NOW ONLY $99
• 75% OFF
• $25 PER VIDEO!
• INSTRUCTIONS FOR IMAGE:
• SHOW PHOTOS OF ALL PHOTOS SIZES USING SAME VIDEO. LET ME KNOW IF YOU NEED ONE I HAVE MP4 FILES FOR ALL SIZES SHOW PHOTOS OF ALL PHOTOS SIZES USING SAME VIDEO. LET ME KNOW IF YOU NEED ONE I HAVE MP4 FILES FOR ALL SIZES OR YOU CAN USE IMAGES FROM MY WEBSITE WWW.LARKREELSTUDIO.COM PLEASE SCROLL DOWN ON HOMEPAGE AND SEE “VIDEO SIEZES” SECTION AND USE THESE IMAGES IF YOU HAVE TO….I WANT THE IMAGE TO SHOW ALL THE DIFFERENT VIDEO SIZES THEY GET SO IT LOOKS LIKE A LOT OF VALUE….
• ___________________________________________________________________________
• LARK MONTHLY CONTENT CALENDAR SUBSCRIPTION:
• Daily Content and Custom Branded Videos For Every Day.
• LESS THAN $10 PER VIDEO!
• INCLUDES:
• 30 Videos ($1470 VALUE)
• VALUE $1470/mth
• 30 Videos & Daily Content Only $299/mth
• 90% OFF
• $10 PER VIDEO!
• INSTRUCTIONS FOR IMAGE:
• SHOW A PIC OF A CALENDAR WITH CONTENT/TEXT AND VIDEO FOR EACH DAY. SEE MY WEBSITE AT https://larkreelstudio.com/calendar/june and use something from here for this image. I WANT IT TO BE CLEAR THAT THEY WILL RECEIVE A VIDEO FOR EVERY DAY AND CONTENT TO POST TO THEIR SOCIAL MEDIA PAGES
• ______________________________________________________________________________
• HOLIDAY THEMED PACKAGE
• Celebrate the Holidays with videos
• $58 PER VIDEO!
• INCLUDES:
• 17 HOLIDAY THEMED VIDEOS ($1683 VALUE)
• VALUE $1683
• 17 Videos Only $999
• 35% OFF
• $58 PER VIDEO!
• INSTRUCTIONS FOR IMAGE:
• SHOW A COLLAGE OF HOLIDAY THEMED VIDEOS. YOU CAN FIND SOME HOLIDAY THEMED VIDEOS ON MY WEBSITE HERE: https://larkreelstudio.com/categories FROM DROP DOWN MENU CHOOSE LABOR DAY, MEMORIAL DAY, HALLOWEEN, CHRISTMAS, NEW YEARS, NEW YEARS, VALENTINES TO SEE EXAMPLES OF HOLIDAY THEMED VIDEOS FOR THIS IMAGE.
• __________________________________________________________________
• SEASONAL THEMED PACKAGE
• Welcome every season with a new video
• $74 PER VIDEO!
• 4 Seasonal Themed Videos ($396 VALUE)
• VALUE $396
• 4 Videos Only $299
• 25% OFF
• $74 PER VIDEO!
• INSTRUCTIONS FOR IMAGE:
• SHOW A COLLAGE OF SEASONAL THEMED VIDEOS. YOU CAN FIND THE SEASONAL THEMED VIDEOS ON MY WEBSITE CLIPNEST PAGE HERE: https://clipnest.com/user41527093 SUMMER, SPRING, FALL, WINTER
Nice to have
• NEED 5 GRAPHICS MADE FOR MY SHOP PAGE HERE: http://pixelcratehub.com/qx/dorian/shop.jpg 900x600
• AL A CARTE:
• $37 PER VIDEO!
• INCLUDES:
• 1 Video Ad ($149 VALUE)
• VALUE $356
• 4 Videos NOW ONLY $149
• 60% OFF
• $37 PER VIDEO!
• INSTRUCTIONS FOR IMAGE:
• SUBSCRIPTION:
• $25 PER VIDEO!
• INCLUDES:
• 1 Video Ad ($149 VALUE)
• VALUE $356
• 4 Videos NOW ONLY $99
• 75% OFF
• $25 PER VIDEO!
• INSTRUCTIONS FOR IMAGE:
• INCLUDES:
• 30 Videos ($1470 VALUE)
• VALUE $1470/mth
• 90% OFF
• $10 PER VIDEO!
• INSTRUCTIONS FOR IMAGE:
• HOLIDAY THEMED PACKAGE
• $58 PER VIDEO!
• INCLUDES:
• VALUE $1683
• 17 Videos Only $999
• 35% OFF
• $58 PER VIDEO!
• INSTRUCTIONS FOR IMAGE:
• SEASONAL THEMED PACKAGE
• $74 PER VIDEO!
• VALUE $396
• 4 Videos Only $299
• 25% OFF
• $74 PER VIDEO!
• INSTRUCTIONS FOR IMAGE:
Should not have
• AL A CARTE:
• $37 PER VIDEO!
• INCLUDES:
• 1 Video Ad ($149 VALUE)
• VALUE $356
• 4 Videos NOW ONLY $149
• 60% OFF
• $37 PER VIDEO!
• INSTRUCTIONS FOR IMAGE:
• SUBSCRIPTION:
• $25 PER VIDEO!
• INCLUDES:
• 1 Video Ad ($149 VALUE)
• VALUE $356
• 4 Videos NOW ONLY $99
• 75% OFF
• $25 PER VIDEO!
• INSTRUCTIONS FOR IMAGE:
• INCLUDES:
• 30 Videos ($1470 VALUE)
• VALUE $1470/mth
• 90% OFF
• $10 PER VIDEO!
• INSTRUCTIONS FOR IMAGE:
• HOLIDAY THEMED PACKAGE
• $58 PER VIDEO!
• INCLUDES:
• VALUE $1683
• 17 Videos Only $999
• 35% OFF
• $58 PER VIDEO!
• INSTRUCTIONS FOR IMAGE:
• SEASONAL THEMED PACKAGE
• $74 PER VIDEO!
• VALUE $396
• 4 Videos Only $299
• 25% OFF
• $74 PER VIDEO!
• INSTRUCTIONS FOR IMAGE:

```html
<!DOCTYPE html>
<html lang="en">
<head>
<meta charset="utf-8">
<title>Al A Carte – Shop Product Graphic</title>
<link rel="stylesheet" href="https://fonts.googleapis.com/css2?family=Arimo:ital,wght@0,400;0,700;1,400&family=Archivo+Black&display=swap">
<style>
  :root {
    --page-bg: #e9e9e9;
    --card-bg: #f6f6f6;
    --navy: #0d2340;
    --accent-line: #29a8e8;
    --title-blue: #1a5ea6;
    --price-blue: #2f8fe0;
    --badge-top: #4ab0f0;
    --badge-bottom: #2a86d8;
    --ink: #111111;
    --sale-red: #f01414;
    --sticker: #ffec00;
    --frame: #ffffff;
    --media-1: #2b3545;
    --media-2: #5b4a44;
    --media-3: #4a4442;
    --media-4: #7fb8e6;
  }
  * { box-sizing: border-box; margin: 0; padding: 0; }
  html, body { width: 1200px; height: 630px; overflow: hidden; }
  body { background: var(--page-bg); font-family: "Arimo", Arial, sans-serif; color: var(--ink); }

  .product-card {
    position: absolute; left: 150px; top: 15px;
    width: 900px; height: 600px;
    background: var(--card-bg); overflow: hidden;
  }
  .diagonal-panel { position: absolute; inset: 0; width: 900px; height: 600px; }

  .offer-title {
    position: absolute; left: 47px; top: 40px;
    font-weight: 700; font-size: 52px; line-height: 1; letter-spacing: -0.5px;
    color: var(--title-blue);
  }
  .offer-tagline {
    position: absolute; left: 47px; top: 92px;
    font-size: 20px; line-height: 1; color: #1b2a44;
  }
  .includes {
    position: absolute; left: 47px; top: 132px;
    font-size: 15.5px; line-height: 25px; list-style: none;
  }

  .price-row { position: absolute; left: 47px; top: 297px; display: flex; align-items: center; }
  .price-badge {
    width: 124px; height: 62px; border-radius: 4px;
    background: linear-gradient(var(--badge-top), var(--badge-bottom));
    color: #fff; display: flex; align-items: center; justify-content: center;
    font-weight: 700; letter-spacing: -1px;
  }
  .price-badge .currency { font-size: 30px; align-self: flex-start; margin-top: 8px; margin-right: 3px; }
  .price-badge .amount { font-size: 56px; line-height: 1; }
  .price-meta { margin-left: 11px; line-height: 1; }
  .price-unit { font-weight: 700; font-size: 32px; color: var(--price-blue); }
  .price-value { font-style: italic; font-size: 24px; margin-top: 2px; }

  .bundle { position: absolute; left: 47px; top: 462px; line-height: 1; }
  .bundle-count { font-weight: 700; font-size: 29px; }
  .bundle-price { font-weight: 700; font-size: 31px; color: var(--sale-red); margin-top: 6px; }

  .discount-sticker {
    position: absolute; left: 326px; top: 356px;
    width: 182px; height: 182px; border-radius: 50%;
    background: var(--sticker);
    display: flex; flex-direction: column; align-items: center; justify-content: center;
    font-family: "Archivo Black", "Arial Black", sans-serif; line-height: 0.9;
  }
  .discount-sticker .pct { font-size: 72px; letter-spacing: -3px; }
  .discount-sticker .pct sup { font-size: 34px; vertical-align: 30px; letter-spacing: 0; }
  .discount-sticker .off { font-size: 54px; letter-spacing: -1px; }

  .video-frame {
    position: absolute; border: 2px solid var(--frame);
    display: flex; align-items: center; justify-content: center;
  }
  .video-frame.vertical  { left: 701px; top: 43px;  width: 159px; height: 265px; background: linear-gradient(#1c1c24, var(--media-1)); }
  .video-frame.landscape { left: 507px; top: 231px; width: 169px; height: 169px; background: linear-gradient(135deg, var(--media-2), #2c2626); }
  .video-frame.small     { left: 704px; top: 329px; width: 171px; height: 95px;  background: linear-gradient(135deg, #6b6260, var(--media-3)); }
  .video-frame.cover     { left: 527px; top: 447px; width: 348px; height: 130px; background: linear-gradient(135deg, #9ccbf0, var(--media-4)); }
  .play-icon { width: 30px; height: 30px; }
</style>
</head>
<body>
  <main class="product-card">
    <svg class="diagonal-panel" viewBox="0 0 900 600" aria-hidden="true">
      <polygon points="653,0 900,0 900,600 313,600" fill="var(--navy)"/>
      <line x1="633" y1="0" x2="296" y2="600" stroke="var(--accent-line)" stroke-width="2"/>
      <line x1="653" y1="5" x2="900" y2="5" stroke="var(--accent-line)" stroke-width="2"/>
    </svg>

    <h1 class="offer-title">AL A CARTE</h1>
    <p class="offer-tagline">BUY VIDEO ADS ON AN AS NEEDED BASIS</p>

    <ul class="includes">
      <li>INCLUDES:</li>
      <li>1 Video Ad&nbsp; ($149 VALUE)</li>
      <li>1 Video Ad Converted To Chatterly Cover Video&nbsp; ($129 VALUE)</li>
      <li>1 Video Ad Converted To Square Ratio&nbsp; ($39 VALUE)</li>
      <li>1 Video Ad Converted To Vertical Ratio&nbsp; ($39 VALUE)</li>
    </ul>

    <div class="price-row">
      <div class="price-badge"><span class="currency">$</span><span class="amount">37</span></div>
      <div class="price-meta">
        <div class="price-unit">PER VIDEO</div>
        <div class="price-value">VALUE&nbsp; $356</div>
      </div>
    </div>

    <div class="bundle">
      <div class="bundle-count">4 Videos</div>
      <div class="bundle-price">NOW ONLY $149</div>
    </div>

    <div class="video-frame vertical" role="img" aria-label="Vertical ratio video ad: event promo still">
      <svg class="play-icon" viewBox="0 0 30 30"><circle cx="15" cy="15" r="13" fill="none" stroke="#fff" stroke-width="2"/><polygon points="12,9 21,15 12,21" fill="#fff"/></svg>
    </div>
    <div class="video-frame landscape" role="img" aria-label="Square ratio video ad: on-this-date highlight still">
      <svg class="play-icon" viewBox="0 0 30 30"><circle cx="15" cy="15" r="13" fill="none" stroke="#fff" stroke-width="2"/><polygon points="12,9 21,15 12,21" fill="#fff"/></svg>
    </div>
    <div class="video-frame small" role="img" aria-label="Standard video ad: presenter in office still">
      <svg class="play-icon" viewBox="0 0 30 30"><circle cx="15" cy="15" r="13" fill="none" stroke="#fff" stroke-width="2"/><polygon points="12,9 21,15 12,21" fill="#fff"/></svg>
    </div>
    <div class="video-frame cover" role="img" aria-label="Cover video: hand holding fruit on blue background">
      <svg class="play-icon" viewBox="0 0 30 30"><circle cx="15" cy="15" r="13" fill="none" stroke="#fff" stroke-width="2"/><polygon points="12,9 21,15 12,21" fill="#fff"/></svg>
    </div>

    <div class="discount-sticker">
      <span class="pct">60<sup>%</sup></span>
      <span class="off">OFF</span>
    </div>
  </main>
</body>
</html>
```